Medical Company in need of Modern business card design for new Wound Care clinic.

Modern business card design for our Woundcare company. Logo and description of services can be found on our website; https://www.tovrel-woundcare.com/

```html
<!DOCTYPE html>
<html lang="en">
<head>
<meta charset="utf-8">
<title>Tovrel Woundcare — Business Card</title>
<link rel="stylesheet" href="https://fonts.googleapis.com/css2?family=Open+Sans:wght@400;600;700&display=swap">
<style>
  :root {
    --stage: #222222;
    --gold: #c08d36;
    --gold-light: #d9a54a;
    --gold-deep: #ad7a2b;
    --ink: #151515;
    --paper: #ffffff;
  }
  * { margin: 0; padding: 0; box-sizing: border-box; }
  html, body { width: 1200px; height: 780px; overflow: hidden; background: var(--stage); }
  body { font-family: "Open Sans", Arial, sans-serif; position: relative; }

  .card {
    position: absolute;
    top: 236px;
    width: 540px;
    height: 308px;
    overflow: hidden;
    box-shadow: 0 10px 30px rgba(0,0,0,.45);
  }
  .card--front { left: 40px; background: var(--paper); }
  .card--back {
    left: 620px;
    background: linear-gradient(135deg, var(--gold-light) 0%, var(--gold) 55%, var(--gold-deep) 100%);
    color: var(--paper);
  }

  .front__band { position: absolute; inset: 0; width: 100%; height: 100%; }

  .wordmark {
    font-family: "Open Sans", Arial, sans-serif;
    font-weight: 600;
    letter-spacing: 4px;
    text-transform: uppercase;
    display: flex;
    align-items: center;
    gap: 10px;
  }
  .wordmark__dot {
    width: 14px; height: 14px; border-radius: 50%;
    background: var(--gold);
  }

  .front__brand {
    position: absolute; top: 34px; right: 34px;
    color: var(--ink); font-size: 17px;
  }

  .holder { position: absolute; left: 44px; top: 100px; }
  .holder__name { color: var(--gold); font-size: 27px; font-weight: 700; line-height: 1.1; }
  .holder__role { color: var(--ink); font-size: 14px; margin-top: 4px; }

  .divider {
    position: absolute; left: 262px; top: 138px;
    width: 1px; height: 92px; background: var(--gold);
  }

  .contacts { position: absolute; left: 282px; top: 136px; list-style: none; }
  .contacts li {
    display: flex; align-items: center; gap: 9px;
    font-size: 14px; color: var(--ink); line-height: 24px;
  }
  .contacts svg { width: 14px; height: 14px; fill: var(--gold); flex: none; }

  .address {
    position: absolute; left: 40px; bottom: 9px;
    color: var(--paper); font-size: 12.5px; letter-spacing: .3px;
  }

  .back__brand {
    position: absolute; left: 0; right: 0; top: 62px;
    justify-content: center;
    font-size: 30px; font-weight: 700; letter-spacing: 6px;
    color: #f3c552;
  }
  .back__brand .wordmark__dot { background: #f3c552; width: 18px; height: 18px; }

  .services { position: absolute; left: 36px; right: 36px; top: 150px; text-align: center; }
  .services__title { font-size: 14px; font-weight: 700; letter-spacing: .5px; margin-bottom: 8px; }
  .services__list { font-size: 13px; line-height: 1.65; }
  .services__list span::before { content: "\2022\00a0"; }
</style>
</head>
<body>

<section class="card card--front" aria-label="Business card front">
  <svg class="front__band" viewBox="0 0 540 308" preserveAspectRatio="none" aria-hidden="true">
    <defs>
      <linearGradient id="bandGold" x1="0" y1="0" x2="1" y2="1">
        <stop offset="0" stop-color="#d9a54a"/>
        <stop offset="1" stop-color="#b07d2e"/>
      </linearGradient>
    </defs>
    <path d="M0,150 C110,250 330,300 540,284 L540,308 L0,308 Z" fill="url(#bandGold)"/>
    <path d="M22,148 C120,240 330,290 520,288" fill="none" stroke="#151515" stroke-width="2.5" stroke-linecap="round"/>
  </svg>

  <div class="wordmark front__brand"><span class="wordmark__dot"></span>Tovrel Woundcare</div>

  <div class="holder">
    <div class="holder__name">Daniel Harrow</div>
    <div class="holder__role">Managing Director</div>
  </div>

  <div class="divider"></div>

  <ul class="contacts">
    <li>
      <svg viewBox="0 0 24 24"><path d="M6.6 10.8a15.1 15.1 0 0 0 6.6 6.6l2.2-2.2a1 1 0 0 1 1-.25 11.4 11.4 0 0 0 3.6.57 1 1 0 0 1 1 1V20a1 1 0 0 1-1 1A17 17 0 0 1 3 4a1 1 0 0 1 1-1h3.5a1 1 0 0 1 1 1c0 1.25.2 2.46.57 3.6a1 1 0 0 1-.25 1z"/></svg>
      972-555-0148
    </li>
    <li>
      <svg viewBox="0 0 24 24"><path d="M7 2h10a2 2 0 0 1 2 2v16a2 2 0 0 1-2 2H7a2 2 0 0 1-2-2V4a2 2 0 0 1 2-2zm0 3v13h10V5zm5 14.2a1 1 0 1 0 0 .01z"/></svg>
      (917) 555-0193
    </li>
    <li>
      <svg viewBox="0 0 24 24"><path d="M12 2a10 10 0 1 0 0 20 10 10 0 0 0 0-20zm6.9 9h-3a15 15 0 0 0-1.3-5.6A8 8 0 0 1 18.9 11zM12 4c.9 1.2 1.8 3.7 1.9 7h-3.8C10.2 7.7 11.1 5.2 12 4zM9.4 5.4A15 15 0 0 0 8.1 11h-3a8 8 0 0 1 4.3-5.6zM5.1 13h3a15 15 0 0 0 1.3 5.6A8 8 0 0 1 5.1 13zM12 20c-.9-1.2-1.8-3.7-1.9-7h3.8c-.1 3.3-1 5.8-1.9 7zm2.6-1.4a15 15 0 0 0 1.3-5.6h3a8 8 0 0 1-4.3 5.6z"/></svg>
      www.tovrel-woundcare.com
    </li>
    <li>
      <svg viewBox="0 0 24 24"><path d="M3 5h18a1 1 0 0 1 1 1v12a1 1 0 0 1-1 1H3a1 1 0 0 1-1-1V6a1 1 0 0 1 1-1zm1 2.3V17h16V7.3l-8 5.4z M5.2 7l6.8 4.6L18.8 7z"/></svg>
      info@tovrel-woundcare.com
    </li>
  </ul>

  <p class="address">2180 Linden Ave Ste 100 PMB 204715 Dallas, TX 75231</p>
</section>

<section class="card card--back" aria-label="Business card back">
  <div class="wordmark back__brand"><span class="wordmark__dot"></span>Tovrel Woundcare</div>

  <div class="services">
    <h2 class="services__title">OUR SERVICES</h2>
    <p class="services__list">
      <span>Hyperbaric Oxygen Therapy (HBO): A Cornerstone of Advanced Wound Care</span><br>
      <span>Debridement</span> <span>Advanced Wound Dressings</span> <span>Bio-engineered Skin</span><br>
      <span>Substitutes</span> <span>Compression Therapy</span> <span>and Edema Management</span>
    </p>
  </div>
</section>

</body>
</html>
```